Nine Rung Ledger Remedy Seminar

I would like a flyer to hand out to participants at the speeches that we give. We are a CPA firm that specializes in entrepreneurs and realtors. We would like a flyer that looks crisp and clean, that integrates our logo and our company colors (shades of blue & gold). We would like the wording to be as laid out in the attached documents, but design is up to you. We would like a picture to go along with each point and are open to ideas. The flyer should be one page, preferably just the front.

Colors
3176b5
fee18a

Requirements
Must have
• Our logo and the wording supplied.
• A picture to go along with each topic.
Nice to have
• Images that pop, clean look, professional.
Should not have
• Look messy.

```html
<!DOCTYPE html>
<html lang="en">
<head>
<meta charset="utf-8">
<title>Nine Rung Ledger Remedy Seminar Agenda</title>
<link href="https://fonts.googleapis.com/css2?family=Bebas+Neue&family=Lato:ital,wght@0,400;0,700;0,900;1,700&family=Libre+Baskerville:ital,wght@1,700&display=swap" rel="stylesheet">
<style>
  :root{
    --brand-blue:#2f5aa8;
    --title-blue:#2b5aa6;
    --title-grey:#8b8d90;
    --track:#a9abae;
    --paper:#fbfbfb;
    --ink:#222;
    --step1:#55a64a; --step1-dark:#3f8f3d;
    --step2:#39b894; --step2-dark:#2aa07f;
    --step3:#1aa8c4; --step3-dark:#1190ab;
    --step4:#5050a6; --step4-dark:#3f3f92;
    --step5:#15949f; --step5-dark:#0e7e89;
    --step6:#8c84b9; --step6-dark:#766ea6;
    --step7:#a6a06c; --step7-dark:#8f8955;
  }
  *{box-sizing:border-box;margin:0;padding:0}
  html,body{width:894px;height:1200px;overflow:hidden;background:var(--paper)}
  .flyer{position:relative;width:894px;height:1200px;background:var(--paper);font-family:Arial,Helvetica,sans-serif}
  .track{position:absolute;inset:0}
  .brand{position:absolute;left:90px;top:78px;width:320px}
  .brand-name{font-family:'Lato',sans-serif;font-weight:900;font-size:46px;color:var(--brand-blue);line-height:1;letter-spacing:-.5px}
  .brand-tag{font-family:'Libre Baskerville',serif;font-style:italic;font-weight:700;font-size:12.5px;color:var(--ink);margin-top:40px}
  .title{position:absolute;left:470px;top:86px;width:370px;text-align:right;font-family:'Bebas Neue',sans-serif;line-height:.95}
  .title-main{font-size:44px;color:var(--title-blue)}
  .title-sub{font-size:46px;color:var(--title-grey)}
  .step{position:absolute;width:166px;height:257px;border-radius:16px;color:#fff;
        background:linear-gradient(180deg,var(--c) 0%,var(--cd) 100%)}
  .step::before{content:"";position:absolute;left:0;right:0;top:0;height:45%;border-radius:16px 16px 0 0;
        background:linear-gradient(180deg,rgba(255,255,255,.18),rgba(255,255,255,0))}
  .step::after{content:"";position:absolute;left:50%;bottom:-40px;transform:translateX(-50%);
        border-left:26px solid transparent;border-right:26px solid transparent;border-top:42px solid var(--cd)}
  .step-text{position:relative;padding:48px 12px 0 13px;font-size:11.4px;line-height:1.32}
  .step-icon{position:absolute;left:50%;top:-30px;transform:translateX(-50%);width:60px;height:60px;border-radius:50%;
        background:#fff;border:3px solid var(--cd);display:flex;align-items:center;justify-content:center;box-shadow:0 1px 3px rgba(0,0,0,.25)}
  .step-icon span{display:block;width:32px;height:32px;border-radius:50%;background:#2b2b2b;opacity:.85}
  .step-num{position:absolute;left:50%;bottom:-96px;transform:translateX(-50%);width:64px;height:64px;border-radius:50%;
        background:var(--cd);display:flex;align-items:center;justify-content:center}
  .step-num b{width:50px;height:50px;border-radius:50%;background:radial-gradient(circle at 40% 35%,#fff,#e4e4e4);
        display:flex;align-items:center;justify-content:center;font-family:'Bebas Neue',sans-serif;font-weight:400;font-size:40px;color:#1d1d1d;padding-top:4px}
  .s1{left:77px;top:280px;--c:var(--step1);--cd:var(--step1-dark)}
  .s2{left:274px;top:280px;--c:var(--step2);--cd:var(--step2-dark)}
  .s3{left:471px;top:280px;--c:var(--step3);--cd:var(--step3-dark)}
  .s4{left:665px;top:280px;--c:var(--step4);--cd:var(--step4-dark)}
  .s5{left:181px;top:660px;--c:var(--step5);--cd:var(--step5-dark)}
  .s6{left:371px;top:660px;--c:var(--step6);--cd:var(--step6-dark)}
  .s7{left:567px;top:660px;--c:var(--step7);--cd:var(--step7-dark)}
  .tagline{position:absolute;left:0;right:0;top:1043px;text-align:center;font-family:'Lato',sans-serif;font-style:italic;font-weight:700;font-size:22px;color:var(--ink)}
  .footer-band{position:absolute;left:0;right:0;top:1086px;height:80px;background:var(--brand-blue);color:#fff;display:flex;align-items:center;font-family:'Lato',sans-serif}
  .footer-brand{padding-left:82px;width:370px;border-right:1px solid rgba(255,255,255,.7);height:44px}
  .footer-brand strong{display:block;font-size:21px;font-weight:700;letter-spacing:1px;line-height:1.05}
  .footer-brand small{font-size:12.5px}
  .footer-address{padding-left:34px;width:246px;font-size:13.5px;line-height:1.35;border-right:1px solid rgba(255,255,255,.7);height:44px;display:flex;flex-direction:column;justify-content:center}
  .footer-phones{padding-left:48px;font-size:14.5px;line-height:1.4}
  .footer-phones div{display:flex;align-items:center;gap:6px}
  .footer-contacts{position:absolute;left:0;right:0;top:1176px;display:flex;justify-content:center;gap:22px;font-family:'Lato',sans-serif;font-size:11.5px;color:var(--brand-blue)}
  .footer-contacts span{display:flex;align-items:center;gap:5px}
</style>
</head>
<body>
<div class="flyer">
  <svg class="track" width="894" height="1200" viewBox="0 0 894 1200" fill="none">
    <path d="M448 42 H797 A60 60 0 0 1 857 102 V161 A60 60 0 0 1 797 221 H105 A60 60 0 0 0 45 281 V543 A60 60 0 0 0 105 603 H797 A60 60 0 0 1 857 663 V924 A60 60 0 0 1 797 984 H140" stroke="var(--track)" stroke-width="2.5"/>
    <circle cx="448" cy="42" r="12" fill="var(--brand-blue)"/>
    <circle cx="140" cy="984" r="12" fill="var(--step5)"/>
  </svg>

  <header class="brand">
    <div class="brand-name">Tallyway Partners</div>
    <div class="brand-tag">A Professional Accounting Corporation</div>
  </header>

  <h1 class="title">
    <div class="title-main">Nine Rung Ledger Remedy</div>
    <div class="title-sub">Seminar Agenda</div>
  </h1>

  <section class="step s1">
    <div class="step-icon"><span role="img" aria-label="Icon of a dollar coupon being cut"></span></div>
    <p class="step-text">We will first show you how to eliminate much of your self-employment tax on your return by converting your business into an S Corporation. A business owner making over $120,000 per year can save about $12,000 per year by doing this.</p>
    <div class="step-num"><b>1</b></div>
  </section>
  <section class="step s2">
    <div class="step-icon"><span role="img" aria-label="Icon of a house with a dollar sign held in a hand"></span></div>
    <p class="step-text">We will show you how to get tax free income from your corporation by renting you home to the corporation for the board meetings. Many of our clients are getting up to $21,000 in tax free income which could put $8,400 cash into your pocket.</p>
    <div class="step-num"><b>2</b></div>
  </section>
  <section class="step s3">
    <div class="step-icon"><span role="img" aria-label="Icon of a magnifying glass over a receipt"></span></div>
    <p class="step-text">We will show you the easiest way to track your expenses so that the only thing you will have to do to have rock solid books is to take a picture of the receipt and throw it away. It doesn't get any better than that.</p>
    <div class="step-num"><b>3</b></div>
  </section>
  <section class="step s4">
    <div class="step-icon"><span role="img" aria-label="Icon of people meeting at a table"></span></div>
    <p class="step-text">Next, we show you the importance of tax planning and why it is critical to meet with your CPA before the end of the year and not just when you do your tax preparation.</p>
    <div class="step-num"><b>4</b></div>
  </section>
  <section class="step s5">
    <div class="step-icon"><span role="img" aria-label="Icon of a parent with children"></span></div>
    <p class="step-text">We will show you how to hire your children and get $7,500 per child tax free. This will save you $3,000 per child in income tax reduction.</p>
    <div class="step-num"><b>5</b></div>
  </section>
  <section class="step s6">
    <div class="step-icon"><span role="img" aria-label="Icon of a graduate in cap and gown"></span></div>
    <p class="step-text">We will discuss how to make your child's college education tax deductible. With college cost spiraling out of control this is a biggie. Most of our clients have a savings of about $12,000 per year of college.</p>
    <div class="step-num"><b>6</b></div>
  </section>
  <section class="step s7">
    <div class="step-icon"><span role="img" aria-label="Icon of a rising bar chart with an arrow"></span></div>
    <p class="step-text">Our grand finale is to show you how to use, not one, but two corporations to get a several hundred thousand dollar tax deferral, get an interest free loan from the government and use that money to grow your business and your wealth.</p>
    <div class="step-num"><b>7</b></div>
  </section>

  <p class="tagline">If they drive by with a machine gun you don't have to stand up.</p>

  <footer>
    <div class="footer-band">
      <div class="footer-brand"><strong>TALLYWAY PARTNERS</strong><small>A Professional Accounting Corporation</small></div>
      <div class="footer-address"><span>2817 Orchard Row, Ste. B,</span><span>Larkfield, CA 95412</span></div>
      <div class="footer-phones">
        <div><svg width="15" height="12" viewBox="0 0 15 12"><path d="M1 4 Q7.5 -1 14 4 L12 6 L10 4.5 L10 3.5 Q7.5 2.5 5 3.5 L5 4.5 L3 6 Z M3 7 H12 L13 11 H2 Z" fill="#fff"/></svg>555-014-2271</div>
        <div><svg width="15" height="12" viewBox="0 0 15 12"><rect x="1" y="5" width="13" height="6" fill="#fff"/><rect x="4" y="1" width="7" height="5" fill="none" stroke="#fff" stroke-width="1.5"/></svg>555-014-2290</div>
      </div>
    </div>
    <div class="footer-contacts">
      <span><svg width="12" height="9" viewBox="0 0 12 9"><rect x=".5" y=".5" width="11" height="8" fill="var(--brand-blue)"/><path d="M.5 .5 L6 5 L11.5 .5" stroke="#fff" fill="none"/></svg>nora@tallywaycpas.com</span>
      <span><svg width="12" height="9" viewBox="0 0 12 9"><rect x=".5" y=".5" width="11" height="8" fill="var(--brand-blue)"/><path d="M.5 .5 L6 5 L11.5 .5" stroke="#fff" fill="none"/></svg>owen@tallywaycpas.com</span>
      <span><svg width="11" height="11" viewBox="0 0 11 11" fill="none" stroke="var(--brand-blue)"><circle cx="5.5" cy="5.5" r="5"/><ellipse cx="5.5" cy="5.5" rx="2.2" ry="5"/><path d="M.5 5.5 H10.5"/></svg>www.tallywaycpa.com</span>
    </div>
  </footer>
</div>
</body>
</html>
```